Leadership Brenvale Brochure Design*

We host a local leadership development program every two years. We need a brochure to promote the program. We would like it to be 8 1/2 x 11, tri-fold. I have attached a Word document with the necessary info for the brochure. The brochure will be professionally printed. We would like the final design to be in InDesign.

Target Market(s)

Potential participants of our leadership program. They will be local leaders, male and female, from 30-60 years of age.

Requirements
Must have
• Content as detailed in the Word document attached. Our logo.
Nice to have
• A design that is attractive to young professionals.

```html
<!DOCTYPE html>
<html lang="en">
<head>
<meta charset="utf-8">
<title>Leadership Brenvale Brochure</title>
<link href="https://fonts.googleapis.com/css2?family=Arimo:wght@400;700&family=Bowlby+One&display=swap" rel="stylesheet">
<style>
:root{
  --green:#3cb44a;
  --blue:#2e3a9c;
  --cyan:#3aa6dc;
  --cyan-dark:#2a86c4;
  --orange:#f08a1c;
  --ink:#222;
  --grey:#555;
  --light:#9a9a9a;
  --black:#121212;
  --paper:#ffffff;
  --bg:#e9e9e9;
}
*{box-sizing:border-box;margin:0;padding:0}
html,body{width:792px;height:1200px;overflow:hidden;background:var(--bg)}
body{font-family:"Arimo",Arial,sans-serif;color:var(--ink)}
.sheet{position:absolute;left:0;width:792px;height:590px;display:flex;background:var(--paper)}
.sheet--outside{top:0}
.sheet--inside{top:610px}
.panel{position:relative;width:264px;height:590px;overflow:hidden}

/* info panel */
.info{padding:30px 22px 0}
.info h3{color:var(--green);font-size:12px;font-weight:700;margin:0 0 5px}
.info p{font-size:8.6px;line-height:1.45;color:var(--grey);margin-bottom:26px}
.info a{color:var(--orange);text-decoration:none}
.call-box{position:absolute;left:0;right:0;bottom:0;height:120px;background:var(--green);color:#fff;text-align:center;padding-top:30px}
.call-box p{font-size:14px;line-height:1.25}
.call-box .phone{font-family:"Bowlby One",sans-serif;font-size:24px;margin-top:6px;letter-spacing:.5px}

/* testimonials */
.alumni{background:linear-gradient(180deg,var(--cyan-dark),var(--cyan));color:#fff;padding:26px 20px 0}
.alumni h2{font-size:15px;font-weight:700;line-height:1.2;margin-bottom:16px}
.quote-head{display:flex;align-items:flex-end;gap:12px;margin-bottom:8px}
.portrait{width:58px;height:58px;background:linear-gradient(160deg,#d8d8d8,#8d8d8d);border:2px solid #fff;flex:none}
.quote-head h4{font-size:12px}
.quote-head small{display:block;font-size:7px;line-height:1.3;font-weight:400;opacity:.9}
.alumni blockquote{font-size:7.6px;line-height:1.42;margin-bottom:20px}

/* cover */
.cover{background:#f3f3f3}
.cover h1{font-family:"Bowlby One",sans-serif;font-weight:400;font-size:17px;line-height:1.08;color:#9b9b9b;padding:20px 20px 0;text-transform:uppercase}
.cover h1 em{font-style:normal;color:var(--orange)}
.cover-art{position:absolute;left:0;top:140px;width:264px;height:210px}
.brand{position:absolute;left:0;right:0;top:385px;display:flex;align-items:center;justify-content:center;gap:8px}
.brand-dot{width:14px;height:14px;border-radius:50%;background:var(--green)}
.brand-name{font-size:19px;font-weight:700;color:var(--blue);letter-spacing:-.2px}
.sponsor-band{position:absolute;left:0;right:0;top:490px;border-top:3px solid var(--blue);padding-top:6px;text-align:center}
.sponsor-band .label{font-size:9px;letter-spacing:4px;color:var(--blue);margin-bottom:6px}
.sponsor-band .bar{height:6px;background:var(--blue);margin-bottom:8px}
.sponsor-band p{font-size:9px;color:var(--grey);line-height:1.35}

/* overview */
.overview{background:var(--black);color:#fff;padding:28px 20px 0}
.tag{display:inline-block;background:var(--green);font-family:"Bowlby One",sans-serif;font-size:14px;padding:4px 12px;margin:0 -20px 14px -20px;padding-left:20px}
.overview p.lead{font-size:10px;line-height:1.42;margin-bottom:28px}
.goals{list-style:none}
.goals li{display:flex;align-items:center;gap:14px;margin-bottom:22px;color:var(--green);font-size:9.6px;line-height:1.3}
.goals svg{flex:none;width:30px;height:30px}

/* schedule */
.schedule-wrap{position:relative;width:528px;height:590px}
.group-photo{position:absolute;left:0;top:0;width:528px;height:150px;background:linear-gradient(100deg,#6d6a5c,#a29882 40%,#8a8a80 70%,#c7c1b3)}
.schedule-title{position:absolute;left:20px;top:162px;display:flex;align-items:center;gap:10px}
.schedule-title h2{font-family:"Bowlby One",sans-serif;font-weight:400;color:var(--blue);font-size:16px}
.schedule-rule{position:absolute;left:0;top:190px;width:264px;height:2px;background:var(--orange)}
.col{position:absolute;top:200px;width:240px}
.col--a{left:24px}
.col--b{left:288px;top:164px}
.event{margin-bottom:10px}
.event h4{color:var(--orange);font-size:11px;font-weight:700}
.event .topic{color:var(--green);font-size:9px}
.event .time{color:var(--light);font-size:8.6px;margin:1px 0 2px}
.event ul{padding-left:14px;font-size:8.2px;line-height:1.32;color:var(--ink)}
</style>
</head>
<body>

<!-- outside of the tri-fold -->
<section class="sheet sheet--outside">
  <div class="panel info">
    <h3>Attendance Policy</h3>
    <p>Attendance at all sessions including the opening retreat is compulsory. Participants may miss no more than one session to graduate; however, the Organizational Retreat is mandatory.</p>
    <h3>Tuition</h3>
    <p>If accepted in the Leadership Brenvale program, you or your employer/sponsor will be invoiced $400 for Chamber members and $500 for non-members. This fee covers costs for the retreat, classroom sessions, lunches, and graduation. No refunds will be provided for participants who drop out of the program or do not fulfill the required curriculum.</p>
    <h3>To Apply</h3>
    <p>Applications are available on the Chamber's website, <a>www.TheBrenvaleChamber.com</a>. Applications are due by November 2, 2020.<br><br>Class size is limited. All applications received by the deadline will be reviewed and final participants for the Leadership Brenvale class will be contacted on December 4, 2020. However, all applicants will be notified of the status of their application in writing.</p>
    <div class="call-box">
      <p>For questions,<br>please call the Chamber</p>
      <div class="phone">555-014-2290</div>
    </div>
  </div>

  <div class="panel alumni">
    <h2>What Community<br>alumni are saying</h2>
    <div class="quote-head">
      <div class="portrait" role="img" aria-label="Portrait photo of alumna Dana Whitfield"></div>
      <h4>Dana Whitfield<small>Co-Owner, Ridgeline Grill</small></h4>
    </div>
    <blockquote>"Leadership Brenvale was an awesome experience! I learned many interesting things about the county that I have lived in all my life. We had very informative panel discussions and the tours of local attractions, including the Fenwick Correctional Facility were eye opening! I enjoyed learning and working beside a great group of folks who are taking leadership roles in our communities to make our county a better place to live, work and play."</blockquote>
    <div class="quote-head">
      <div class="portrait" role="img" aria-label="Portrait photo of alumnus Owen R. Haskell"></div>
      <h4>Owen R. Haskell<small>CPA, Partner/Manager of the Marlow Office<br>Halvorsen Carter &amp; Associates, LLP</small></h4>
    </div>
    <blockquote>For the first year and a half I was working at Halvorsen Carter, I commuted from Bayport, so I was not involved in the community at all. Once we moved here, I knew I wanted and felt I had to become more involved. I learned about the program through a colleague. I couldn't have asked for a better experience and it really exposed me to the many ways that I could get involved and contribute to the chamber and our community. I didn't know a soul in that 2014 class when it started and now many of them are my very best friends. If you have an opportunity to go through Leadership Brenvale you would be crazy to pass it up. It is the best program the Chamber has and, quite frankly, one of the best opportunities to better yourself in this community.</blockquote>
  </div>

  <div class="panel cover">
    <h1>The greatest wealth of a community lies not in the amount of its treasure, <em>but in the quality of its leadership.</em></h1>
    <svg class="cover-art" viewBox="0 0 264 210" aria-hidden="false">
      <polygon points="0,150 0,210 70,210 264,70 264,20" fill="#2e3a9c"/>
      <polygon points="92,8 176,8 224,100 176,192 92,192 44,100" fill="#fff"/>
      <polygon points="96,14 172,14 216,100 172,186 96,186 52,100" fill="#8f8f8f" role="img" aria-label="Black and white photo of joined hands in a circle"/>
    </svg>
    <div class="brand">
      <span class="brand-dot"></span>
      <span class="brand-name">Leadership Brenvale</span>
    </div>
    <div class="sponsor-band">
      <div class="label">SPONSORED BY</div>
      <div class="bar"></div>
      <p>Lowland Community College<br>Brenvale Chamber of Commerce and Tourism</p>
    </div>
  </div>
</section>

<!-- inside of the tri-fold -->
<section class="sheet sheet--inside">
  <div class="panel overview">
    <div class="tag">PROGRAM OVERVIEW</div>
    <p class="lead">Leadership Brenvale is a leadership certification program designed to prepare the leaders of tomorrow. During the five-month program, participants get an in-depth view of community issues, develop leadership skills necessary to assume leadership roles, and are exposed to community involvement opportunities. Leadership Brenvale will provide participants with the opportunities to:</p>
    <ul class="goals">
      <li><svg viewBox="0 0 30 30" fill="none" stroke="#fff" stroke-width="1.6"><circle cx="8" cy="9" r="3"/><circle cx="15" cy="7" r="3"/><circle cx="22" cy="9" r="3"/><path d="M3 24v-6a5 5 0 0 1 10 0v6M10 22v-7a5 5 0 0 1 10 0v7M17 24v-6a5 5 0 0 1 10 0v6"/></svg>Build and demonstrate leadership and communication skills</li>
      <li><svg viewBox="0 0 30 30" fill="none" stroke="#fff" stroke-width="1.6"><path d="M15 4a8 8 0 0 0-5 14v4h10v-4A8 8 0 0 0 15 4z"/><path d="M11 25h8"/></svg>Think critically about key business, policy, and civic issues facing Brenvale County</li>
      <li><svg viewBox="0 0 30 30" fill="none" stroke="#fff" stroke-width="2"><rect x="4" y="13" width="13" height="7" rx="3.5" transform="rotate(-45 10 16)"/><rect x="13" y="10" width="13" height="7" rx="3.5" transform="rotate(-45 20 13)"/></svg>Build meaningful, long-lasting connections</li>
      <li><svg viewBox="0 0 30 30" fill="none" stroke="#fff" stroke-width="1.6"><rect x="8" y="3" width="14" height="9" rx="1"/><circle cx="6" cy="16" r="2.5"/><circle cx="24" cy="16" r="2.5"/><path d="M3 27v-4a3 3 0 0 1 6 0v4M21 27v-4a3 3 0 0 1 6 0v4M10 21h10"/></svg>Establish ongoing dialogues with experienced community leaders</li>
    </ul>
  </div>

  <div class="schedule-wrap">
    <div class="group-photo" role="img" aria-label="Group photo of a past Leadership Brenvale class"></div>
    <div class="schedule-title">
      <svg width="22" height="20" viewBox="0 0 22 20" fill="none" stroke="#3cb44a" stroke-width="1.4"><rect x="1" y="3" width="20" height="16" rx="1"/><path d="M1 7h20M6 1v4M16 1v4M5 10h2M10 10h2M15 10h2M5 14h2M10 14h2M15 14h2"/></svg>
      <h2>SCHEDULE</h2>
    </div>
    <div class="schedule-rule"></div>

    <div class="col col--a">
      <div class="event">
        <h4>January 17</h4>
        <div class="topic">Organizational Retreat &amp; Dinner<br>(Attendance Mandatory)</div>
        <div class="time">10:00 a.m. – 7:00 p.m.</div>
        <ul><li>Introductions</li><li>Team Building</li><li>Motivation</li><li>Leadership Styles</li><li>Social Hour/Dinner</li></ul>
      </div>
      <div class="event">
        <h4>January 31</h4>
        <div class="topic">Business &amp; Industry</div>
        <div class="time">8:30 a.m. – 4:00 p.m.</div>
        <ul><li>Business &amp; Industry panel discussion</li><li>Tour of Stenwick Plant facility</li><li>Tour of Council offices</li><li>Taking your vision to market</li></ul>
      </div>
      <div class="event">
        <h4>February 21</h4>
        <div class="topic">Education</div>
        <div class="time">8:30 a.m. – 4:00 p.m.</div>
        <ul><li>Tour of select county schools</li><li>College Career Center visit</li><li>Lunch at LCC culinary program</li><li>College Access panel</li><li>Tour of LCC campus</li><li>Overview of public education</li></ul>
      </div>
    </div>

    <div class="col col--b">
      <div class="event">
        <h4>March 14</h4>
        <div class="topic">Future Technologies &amp; Communications</div>
        <div class="time">8:30 a.m. – 4:00 p.m.</div>
        <ul><li>LCC Presents interview</li><li>Trends and forecasts</li><li>Marketing &amp; communications panel</li></ul>
      </div>
      <div class="event">
        <h4>April 4</h4>
        <div class="topic">Government</div>
        <div class="time">8:30 a.m. – 4:00 p.m.</div>
        <ul><li>Overview of state/federal government</li><li>Overview of city/county government</li><li>Tour of Fenwick Correctional Institute</li><li>Tour of courthouse</li><li>Judicial presentations</li></ul>
      </div>
      <div class="event">
        <h4>May 02</h4>
        <div class="topic">Health &amp; Wellness</div>
        <div class="time">8:30 a.m. – 4:00 p.m.</div>
        <ul><li>Tour of Lower Riverbend Hospice</li><li>Community Wellness Roundtable</li><li>Tour of Ashgrove Cancer Care Center</li><li>Virtual Medicine Tutorial</li><li>Tour of BRHS</li></ul>
      </div>
      <div class="event">
        <h4>May 18</h4>
        <div class="topic">Graduation Ceremony and Luncheon</div>
        <div class="time">(12:00 p.m.)</div>
        <ul><li>Participants are encouraged to invite their employer/supervisor/mentor/special guest (x2)</li></ul>
      </div>
    </div>
  </div>
</section>

</body>
</html>
```